I need a new business card design for my pharmacy.

I need a business card design. I will include my logo.
The card needs to be readable. I prefer to have my logo on one side along with my website, the other side includes the other information. Please use combination of black, neon green, white, and silver. This needs to catch the eye but yet be clearly visible and legible. Thanks

Industry/Entity Type

Pharmacy

Contact Information for Business Card

It needs to have the following information listed:
Mel's Apothecary Owner/Pharm D.
7134 North Brook Lane
Sioux Falls, SD 57231
Phone 605-318-6207
Fax 605-318-6209
email: mel@melsapothecary-example.com
www.melsapothecary-example.com
Store hours Monday-Friday 8 am- 7 pm
Saturday 8 am- 12 pm
Sunday Closed
Please utilize the colors black, white, and neon green, maybe silver.

Requirements
Must have
• It needs to be easily readable!
Nice to have
• It should catch the eye.
Should not have
• Do not use any other colors except listed: black, neon green, white, & silver.

```html
<!DOCTYPE html>
<html lang="en">
<head>
<meta charset="utf-8">
<title>Mel's Apothecary – Business Card</title>
<link rel="stylesheet" href="https://fonts.googleapis.com/css2?family=Dosis:wght@400;500&family=Arimo:wght@400;700&display=swap">
<style>
  :root {
    --leaf-green: #a8cf3a;
    --paper-white: #ffffff;
    --ink-black: #1a1a1a;
    --silver-light: #f1f1f3;
    --silver-mid: #dcdcdf;
    --silver-dark: #c9c9cd;
  }
  * { box-sizing: border-box; margin: 0; padding: 0; }
  html, body { width: 1200px; height: 667px; overflow: hidden; background: var(--paper-white); }
  .card {
    position: relative;
    width: 1200px;
    height: 667px;
    background: var(--leaf-green);
    overflow: hidden;
    font-family: "Arimo", Arial, sans-serif;
  }
  .card__texture {
    position: absolute;
    inset: 0;
    width: 1200px;
    height: 667px;
  }
  .card__title {
    position: absolute;
    left: 50px;
    top: 101px;
    max-width: 660px;
    font-family: "Dosis", sans-serif;
    font-weight: 400;
    font-size: 48px;
    line-height: 1;
    color: var(--paper-white);
    white-space: nowrap;
    letter-spacing: 0;
  }
  .card__rule {
    position: absolute;
    left: 135px;
    top: 189px;
    width: 424px;
    height: 1px;
    background: var(--paper-white);
  }
  .contact {
    position: absolute;
    left: 108px;
    top: 222px;
    list-style: none;
    color: var(--paper-white);
    font-size: 25px;
    line-height: 38px;
  }
  .contact__item {
    position: relative;
    padding-left: 58px;
    white-space: nowrap;
  }
  .contact__item--address { margin-bottom: 18px; }
  .contact__item--phone { margin-bottom: 24px; }
  .contact__item--fax { margin-bottom: 26px; }
  .contact__icon {
    position: absolute;
    left: 0;
    top: 2px;
    width: 40px;
    height: 36px;
    fill: var(--paper-white);
  }
  .hours {
    position: absolute;
    left: 0;
    top: 508px;
    width: 800px;
    text-align: center;
    color: var(--ink-black);
    font-size: 27px;
    line-height: 42px;
  }
  .hours__label { text-decoration: underline; text-underline-offset: 4px; text-decoration-thickness: 1px; }
  .hours__closed { font-weight: 700; }
</style>
</head>
<body>
<main class="card">
  <svg class="card__texture" viewBox="0 0 1200 667" role="img" aria-label="Silver geometric cube texture panel">
    <defs>
      <linearGradient id="silverPanel" x1="0" y1="0" x2="1" y2="1">
        <stop offset="0" stop-color="#f3f3f5"/>
        <stop offset="0.5" stop-color="#e2e2e5"/>
        <stop offset="1" stop-color="#d2d2d6"/>
      </linearGradient>
      <filter id="panelShadow" x="-10%" y="-10%" width="130%" height="130%">
        <feDropShadow dx="-6" dy="6" stdDeviation="6" flood-color="#000" flood-opacity="0.35"/>
      </filter>
    </defs>
    <polygon filter="url(#panelShadow)" fill="url(#silverPanel)"
      points="615,0 723,73 723,497 841,565 841,667 1200,667 1200,0"/>
  </svg>

  <h1 class="card__title">Mel’s Apothecary Owner/Pharm D</h1>
  <div class="card__rule"></div>

  <ul class="contact">
    <li class="contact__item contact__item--address">
      <svg class="contact__icon" viewBox="0 0 40 36" aria-hidden="true">
        <polygon points="20,2 2,17 6,17 20,6 34,17 38,17"/>
        <rect x="28" y="4" width="4" height="8"/>
        <path d="M8,18 L20,9 L32,18 L32,34 L23,34 L23,24 L17,24 L17,34 L8,34 Z"/>
      </svg>
      7134 North Brook Lane,<br>Sioux Falls, SD 57231
    </li>
    <li class="contact__item contact__item--phone">
      <svg class="contact__icon" viewBox="0 0 40 40" aria-hidden="true">
        <path d="M9,3 C11,2 13,3 14,5 L17,12 C18,14 17,15 16,16 L14,18 C15,22 19,27 23,29 L25,27 C26,26 28,25 30,26 L36,30 C38,31 38,33 37,35 L35,37 C33,39 29,39 25,37 C16,33 8,24 5,15 C3,10 4,6 6,5 Z"/>
      </svg>
      605-318-6207
    </li>
    <li class="contact__item contact__item--fax">
      <svg class="contact__icon" viewBox="0 0 40 36" aria-hidden="true">
        <rect x="10" y="2" width="20" height="9" rx="1"/>
        <path d="M6,12 H34 A4,4 0 0 1 38,16 V27 H31 V21 H9 V27 H2 V16 A4,4 0 0 1 6,12 Z"/>
        <rect x="11" y="23" width="18" height="11"/>
      </svg>
      605-318-6209
    </li>
    <li class="contact__item contact__item--email">
      <svg class="contact__icon" viewBox="0 0 40 36" aria-hidden="true">
        <path d="M2,14 L20,2 L38,14 V34 H2 Z M10,10 V20 L20,26 L30,20 V10 Z"/>
        <rect x="13" y="12" width="14" height="2"/>
        <rect x="13" y="16" width="14" height="2"/>
      </svg>
      mel@melsapothecary-example.com
    </li>
  </ul>

  <section class="hours">
    <p><span class="hours__label">Store hours</span>:</p>
    <p>Monday-Friday 8 am- 7 pm Saturday 8 am- 12 pm</p>
    <p class="hours__closed">Sunday Closed</p>
  </section>
</main>
</body>
</html>
```